Marketing Software requires Fun and Young Business Card Design

We are looking for a new business card design for a start-up marketing campaign management software that is

- fun
- young/fresh
- engaging
- playful
- new kid on the blog
- wants to catch attention

Check out our website: www.zintaropq.com and watch the first video on the homepage. That way you will get a good picture of the product and the target group.

The current business card (attached) is too mainstream and does not catch the attention that we are looking for.
Attached you will find the company logo, some support images from our website and the current business card design.

Company colours: Zintaro Green
RGB 166 / 176 / 12
CMYK needs conversion

Company font:
Titillium for logo copy
Calibri for content copy

Target Market(s)

- marketing people - design, ad and marketing agency people - main market location: Western Europe and North America

Industry/Entity Type

Marketing

Requirements
Must have
• Information that we would like to have on the BC:
Name: Martin Oakes
Function: CEO
Email: martino@zintaropq.com
Mobile: +44 7912 584 207
Website: www.zintaropq.com (maybe)
Nice to have
• In the supporting files you will find some images from the website that could be reused but is not essential.
We liked the idea of the origami look and feel however this might not necessarily the winner.
We also like our robot from our video on the website www.zintaropq.com.
A call to action to try our product for free might be nice (get a free trial@www.zintaropq.com)

We are looking forward to seeing something new than the standard business card.

```html
<!DOCTYPE html>
<html lang="en">
<head>
<meta charset="utf-8">
<title>Zintaro – Business Card</title>
<link rel="stylesheet" href="https://fonts.googleapis.com/css2?family=Titillium+Web:wght@300;400;700&family=Carlito:wght@400;700&display=swap">
<style>
  :root {
    --page-bg: #f1f0ee;
    --card-front: #e9ebeb;
    --paper-light: #f1f2f3;
    --paper-dark: #d9dcdf;
    --zintaro-green: #a6b00c;
    --green-bright: #b8cc1c;
    --green-mid: #7fb82a;
    --ink: #1e1f22;
    --ink-soft: #3a3c40;
    --band-blue: #2b2f91;
    --robot-grey: #a9a8b8;
  }
  * { margin: 0; padding: 0; box-sizing: border-box; }
  html, body { width: 1200px; height: 880px; overflow: hidden; }
  body {
    background: var(--page-bg);
    font-family: "Carlito", "Calibri", sans-serif;
    position: relative;
  }
  .card {
    position: absolute;
    top: 265px;
    width: 540px;
    height: 350px;
    overflow: hidden;
    box-shadow: 0 6px 18px rgba(0,0,0,0.18);
  }
  .card-front { left: 40px; background: var(--card-front); }
  .card-back {
    left: 620px;
    background: linear-gradient(135deg, var(--paper-light), var(--paper-dark));
  }
  .card-art { position: absolute; inset: 0; width: 100%; height: 100%; }

  .brand { position: absolute; left: 70px; top: 28px; }
  .brand-name {
    display: flex; align-items: center; gap: 14px;
    font-family: "Titillium Web", sans-serif;
    font-weight: 700; font-size: 54px; line-height: 1;
    color: var(--ink); letter-spacing: -0.5px;
  }
  .brand-mark { width: 20px; height: 20px; background: var(--zintaro-green); }
  .brand-tagline {
    font-family: "Titillium Web", sans-serif;
    font-weight: 300; font-size: 24px; color: var(--ink-soft);
    margin-top: 2px;
  }

  .person { position: absolute; left: 160px; top: 170px; color: var(--ink); }
  .person-name { font-weight: 700; font-size: 21px; line-height: 1.1; }
  .person-role { font-size: 13px; margin-top: 3px; }
  .divider {
    position: absolute; left: 330px; top: 172px;
    width: 1px; height: 108px; background: var(--ink);
  }
  .contact {
    position: absolute; left: 344px; top: 174px;
    list-style: none; font-size: 14px; line-height: 26px; color: var(--ink);
  }
  .contact .label { display: inline-block; width: 22px; }

  .robot {
    position: absolute; left: 190px; top: 70px;
    width: 150px; height: 215px;
    background: linear-gradient(180deg, #b3b2c1, var(--robot-grey));
  }
  .slogan {
    position: absolute; left: 370px; top: 112px;
    width: 150px; height: 52px;
    background: linear-gradient(90deg, var(--green-bright), var(--green-mid));
    display: flex; align-items: center; justify-content: center; gap: 6px;
    color: var(--ink);
  }
  .slogan-small { font-size: 12px; }
  .slogan-bold { font-weight: 700; font-size: 21px; }
</style>
</head>
<body>

<section class="card card-front" aria-label="Business card front">
  <svg class="card-art" viewBox="0 0 540 350" aria-hidden="true">
    <defs>
      <linearGradient id="band" x1="0" y1="0" x2="1" y2="0">
        <stop offset="0" stop-color="#b7cc1e"/>
        <stop offset="1" stop-color="#7fb82a"/>
      </linearGradient>
    </defs>
    <rect class="info-band" x="0" y="156" width="540" height="136" fill="url(#band)"/>
  </svg>

  <div class="brand">
    <div class="brand-name"><span>Zintaro</span><span class="brand-mark"></span></div>
    <div class="brand-tagline">marketing collaboration</div>
  </div>

  <div class="person">
    <div class="person-name">Martin Oakes</div>
    <div class="person-role">CEO</div>
  </div>
  <div class="divider"></div>
  <ul class="contact">
    <li>martino@zintaropq.com</li>
    <li><span class="label">m:</span>+44 7912 584 207</li>
    <li><span class="label">t:</span>+44 20 7581 3926</li>
    <li>www.zintaropq.com</li>
  </ul>
</section>

<section class="card card-back" aria-label="Business card back">
  <svg class="card-art" viewBox="0 0 540 350" aria-hidden="true">
    <rect class="floor-band" x="0" y="326" width="540" height="24" fill="var(--band-blue)"/>
  </svg>
  <div class="robot" role="img" aria-label="Illustration of the friendly paper-cut robot mascot"></div>
  <div class="slogan">
    <span class="slogan-small">make</span>
    <span class="slogan-bold">it yours</span>
  </div>
</section>

</body>
</html>
```